Modern and professional facebook ad for disability service

Design a facebook ad for a disability service. Want something bright and fun and eyecatching. Would ideally like a carousel ad as this will give us more options to provide information.
CONTENT:
- Looking for a Plan Manager who will support your QRTA journey so that you can focus on living your best possible life and achieve your QRTA Goals?
- Then join the Bluegate Plan Management family today - quick and easy sign up.
- Friendly, Reliable, Responsive Service
- Dedicate Plan Managers so you always speak to the same person
- Fast Payment of Provider Invoices
- Supporting you to live Your Life, Your Way
- Call us today on 1300 482 613
- www.bluegateplanmanagement.com.au

Target Market(s)

Disability Sector

Other font styles liked:
• Raleway

Requirements
Must have
• Bright colours and eye catching design

```html
<!DOCTYPE html>
<html lang="en">
<head>
<meta charset="utf-8">
<title>Bluegate Plan Management – Carousel Ad</title>
<link href="https://fonts.googleapis.com/css2?family=Poppins:wght@300;400;600;700&display=swap" rel="stylesheet">
<style>
  :root{
    --magenta:#a8306a;
    --teal:#0f7f7a;
    --purple:#6a2a82;
    --grey:#6b6b6b;
    --bg:#b9ae9b;
    --white:#ffffff;
    --photo-a:#dfe3e8;
    --photo-b:#9aa6b8;
  }
  *{box-sizing:border-box;margin:0;padding:0}
  html,body{width:1200px;height:653px;overflow:hidden}
  body{background:var(--bg);font-family:"Poppins",sans-serif;color:var(--grey)}
  .carousel{position:absolute;left:25px;top:213px;display:flex;gap:6px}
  .card{position:relative;width:226px;height:226px;background:var(--white);overflow:hidden;box-shadow:0 8px 14px rgba(0,0,0,.18)}
  .card--double{width:453px}
  .seam{position:absolute;left:226px;top:0;width:1px;height:100%;background:#e2e2e2;z-index:3}
  .abs{position:absolute}
  .brand{position:absolute;font-weight:700;font-size:11px;color:var(--white);line-height:1.1;z-index:4}
  .brand--dark{color:var(--magenta)}
  .brand small{display:block;font-weight:400;font-size:6px;letter-spacing:.3px}
  .photo{position:absolute;background:linear-gradient(145deg,var(--photo-a),var(--photo-b));overflow:hidden}
  .photo--round{border-radius:50%;border:3px solid var(--teal)}
  .badge{position:absolute;border-radius:50%;background:var(--purple);border:2px solid var(--white);z-index:4}
  .pill{position:absolute;font-size:7.5px;font-weight:700;color:var(--white);padding:2px 9px;border-radius:10px;letter-spacing:.4px;z-index:4}
  .pill--magenta{background:var(--magenta)}
  .pill--teal{background:var(--teal)}
  .call{position:absolute;display:flex;align-items:center;gap:3px;z-index:4}
  .call svg{width:12px;height:12px;fill:var(--magenta)}
  .call-label{font-size:4.8px;line-height:1}
  .call-number{font-size:8px;font-weight:700;color:var(--teal);line-height:1}
  .web{position:absolute;font-size:4.4px;font-weight:600;color:var(--teal);z-index:4}
  .social{position:absolute;display:flex;gap:3px;z-index:4}
  .social span{width:8px;height:8px;border-radius:50%;background:var(--magenta)}
  .t{line-height:13px;font-size:9.3px}
  .b{font-weight:700}
  .m{color:var(--magenta)}
  .tl{color:var(--teal)}
  .r{text-align:right}
</style>
</head>
<body>
<div class="carousel">

  <!-- Card 1: plan manager question -->
  <section class="card">
    <div class="abs" style="left:-42px;top:-72px;width:128px;height:128px;border-radius:50%;background:var(--magenta);border:3px solid var(--teal)"></div>
    <div class="brand" style="left:10px;top:16px">Bluegate<small>Plan Management</small></div>
    <div class="photo photo--round" style="left:132px;top:22px;width:178px;height:178px" role="img" aria-label="Photo of a smiling support worker talking with a client at a desk"></div>
    <div class="badge" style="left:118px;top:54px;width:52px;height:52px"></div>
    <div class="abs" style="left:12px;top:60px">
      <p class="t">Looking For</p>
      <p class="t b m">A Plan Manager</p>
      <p class="t">Who Will Support</p>
      <p class="t b tl">Your QRTA Journey</p>
      <p class="t">So That You Can</p>
      <p class="t">Focus On Living Your</p>
      <p class="t b m">Best Possible</p>
      <p class="t b tl">Life And Achieve</p>
      <p class="t b tl">Your QRTA Goals?</p>
    </div>
    <div class="pill pill--magenta" style="left:12px;top:185px">SIGN UP</div>
    <div class="call" style="left:10px;top:206px">
      <svg viewBox="0 0 24 24"><path d="M3 9c0-3 4-5 9-5s9 2 9 5v2h-5V9c-1-1-7-1-8 0v2H3zM6 12h12l2 8H4z"/></svg>
      <div><p class="call-label">Call us today on</p><p class="call-number">1300 482 613</p></div>
    </div>
    <p class="web" style="left:88px;top:212px">www.bluegateplanmanagement.com.au</p>
    <div class="social" style="left:178px;top:210px"><span></span><span></span><span></span></div>
  </section>

  <!-- Card 2: join the family -->
  <section class="card">
    <div class="photo photo--round" style="left:-44px;top:18px;width:192px;height:192px" role="img" aria-label="Photo of a young man assisting a wheelchair user"></div>
    <div class="abs" style="left:152px;top:0;width:74px;height:50px;background:var(--teal);border-bottom-left-radius:28px"></div>
    <div class="brand" style="left:166px;top:12px">Bluegate<small>Plan Management</small></div>
    <div class="abs r" style="right:10px;top:60px;font-size:15px;font-weight:300;line-height:18px">
      <p>Then Join</p><p>The Bluegate</p>
    </div>
    <div class="abs" style="left:46px;right:0;top:102px;height:22px;background:var(--magenta);border-radius:11px 0 0 11px;color:var(--white);font-weight:700;font-size:15px;line-height:22px;padding-left:8px">Plan Management</div>
    <p class="abs b tl r" style="right:10px;top:126px;font-size:15px">Family Today</p>
    <div class="abs" style="right:10px;top:148px;width:60px;height:2px;background:var(--grey)"></div>
    <p class="abs m" style="right:10px;top:156px;font-size:8.5px;font-weight:600">Quick And Easy Sign Up.</p>
    <div class="pill pill--teal" style="right:14px;top:178px">SIGN UP</div>
    <div class="social" style="left:10px;top:210px"><span></span><span></span><span></span></div>
    <p class="web" style="left:42px;top:212px">www.bluegateplanmanagement.com.au</p>
    <div class="call" style="left:138px;top:203px">
      <svg viewBox="0 0 24 24"><path d="M3 9c0-3 4-5 9-5s9 2 9 5v2h-5V9c-1-1-7-1-8 0v2H3zM6 12h12l2 8H4z"/></svg>
      <div><p class="call-label">Call us today on</p><p class="call-number">1300 482 613</p></div>
    </div>
  </section>

  <!-- Cards 3 + 4: service values and dedicated managers -->
  <section class="card card--double">
    <svg class="abs" style="left:0;top:0" width="453" height="226" viewBox="0 0 453 226">
      <circle cx="285" cy="290" r="150" fill="none" stroke="var(--magenta)" stroke-width="32"/>
    </svg>
    <div class="photo" style="left:170px;top:8px;width:150px;height:218px;border-radius:60px 60px 0 0;z-index:2" role="img" aria-label="Photo of a smiling man pushing a woman in a wheelchair"></div>
    <div class="seam"></div>

    <div class="abs" style="left:0;top:0;width:68px;height:48px;background:var(--teal);border-bottom-right-radius:28px"></div>
    <div class="brand" style="left:8px;top:12px">Bluegate<small>Plan Management</small></div>
    <div class="abs" style="left:14px;top:62px;width:2px;height:88px;background:var(--magenta)"></div>
    <div class="abs" style="left:20px;top:60px;font-size:17px;font-weight:700;line-height:22px">
      <p>Friendly</p><p>Reliable</p><p class="m">Responsive</p><p class="tl">Service</p>
    </div>
    <div class="pill pill--teal" style="left:16px;top:162px">SIGN UP</div>
    <div class="call" style="left:12px;top:186px">
      <svg viewBox="0 0 24 24"><path d="M3 9c0-3 4-5 9-5s9 2 9 5v2h-5V9c-1-1-7-1-8 0v2H3zM6 12h12l2 8H4z"/></svg>
      <div><p class="call-label">Call us today on</p><p class="call-number">1300 482 613</p></div>
    </div>
    <p class="web" style="left:12px;top:208px;font-size:6px">www.bluegateplanmanagement.com.au</p>
    <div class="social" style="left:166px;top:206px"><span></span><span></span><span></span></div>

    <div class="call" style="left:240px;top:10px">
      <svg viewBox="0 0 24 24" style="width:16px;height:16px"><path d="M3 9c0-3 4-5 9-5s9 2 9 5v2h-5V9c-1-1-7-1-8 0v2H3zM6 12h12l2 8H4z"/></svg>
      <div><p class="call-label" style="font-size:6px">Call us today on</p><p class="call-number" style="font-size:10.5px">1300 482 613</p></div>
    </div>
    <div class="brand brand--dark" style="left:392px;top:14px">Bluegate<small>Plan Management</small></div>
    <div class="abs r" style="right:10px;top:60px;font-size:12.5px;line-height:16px">
      <p class="b m">Dedicate</p><p class="b tl">Plan Managers</p>
      <p>So You Always</p><p>Speak To</p><p>The Same Person</p>
    </div>
    <div class="badge" style="left:336px;top:152px;width:56px;height:56px"></div>
    <div class="pill pill--magenta" style="left:398px;top:173px">SIGN UP</div>
    <div class="social" style="left:400px;top:200px"><span style="width:11px;height:11px;background:var(--teal)"></span><span style="width:11px;height:11px;background:var(--teal)"></span><span style="width:11px;height:11px;background:var(--teal)"></span></div>
    <p class="web" style="left:240px;top:211px">www.bluegateplanmanagement.com.au</p>
  </section>

  <!-- Card 5: fast payment -->
  <section class="card">
    <div class="abs" style="left:16px;top:0;width:90px;height:112px;background:var(--magenta)"></div>
    <div class="abs b" style="left:16px;top:8px;width:90px;text-align:center;color:var(--white);font-size:12.5px;line-height:14px">
      <p>Fast<br>Payment<br>Of</p><p style="font-size:11px">Provider</p><p style="font-size:15px">Invoices</p>
    </div>
    <div class="photo photo--round" style="left:8px;top:92px;width:108px;height:108px" role="img" aria-label="Photo of a support worker reviewing a tablet with a man in a wheelchair"></div>
    <div class="brand brand--dark" style="left:168px;top:12px">Bluegate<small>Plan Management</small></div>
    <div class="abs r" style="right:10px;top:66px;line-height:11px">
      <p style="font-size:8.5px;font-weight:600">Supporting</p><p style="font-size:8.5px;font-weight:600">you to</p>
      <p class="b tl" style="font-size:13px;line-height:15px;margin-top:2px">live Your</p>
      <p class="b tl" style="font-size:13px;line-height:15px">Life Your Way</p>
    </div>
    <div class="pill pill--magenta" style="right:10px;top:124px">SIGN UP</div>
    <div class="abs" style="right:0;top:148px;width:44px;height:22px;border:1.5px solid var(--teal);border-right:none;border-radius:11px 0 0 11px;display:flex;align-items:center;justify-content:center">
      <svg viewBox="0 0 24 24" width="14" height="14" fill="var(--magenta)"><path d="M3 9c0-3 4-5 9-5s9 2 9 5v2h-5V9c-1-1-7-1-8 0v2H3zM6 12h12l2 8H4z"/></svg>
    </div>
    <p class="abs r" style="right:10px;top:174px;font-size:8.5px;font-weight:600">Call us today on</p>
    <p class="abs b tl r" style="right:10px;top:184px;font-size:14px">1300 482 613</p>
    <p class="web" style="left:12px;top:211px;font-size:6px">www.bluegateplanmanagement.com.au</p>
    <div class="social" style="left:176px;top:209px"><span style="width:10px;height:10px"></span><span style="width:10px;height:10px"></span><span style="width:10px;height:10px"></span></div>
  </section>

</div>
</body>
</html>
```